Wine Label Design

We need a wine label design with the following characteristics:
- Round
- I've attached a photo of a rough design
- The writing:
--- Twin Ks
---Crafted by Lu Venkova
-----Pinwheel Chardonnay
------Dundee Hills
-----2021
- We'd like a couple of options on the background color:
- Pale mint green
- Cream
- Lettering a dark gray
- The three cursive Ms should kinda look like mountains
- Size: 3"x3"

```html
<!DOCTYPE html>
<html lang="en">
<head>
<meta charset="utf-8">
<title>Twin Ks – Pinwheel Chardonnay Label Options</title>
<link rel="stylesheet" href="https://fonts.googleapis.com/css2?family=Cormorant+Garamond:wght@600&family=Cormorant+SC:wght@600&display=swap">
<style>
  :root {
    --board: #4d4d4d;
    --ink: #666666;
    --mint: #d1e2cc;
    --cream: #fefdd8;
  }
  html, body {
    margin: 0;
    padding: 0;
    width: 1200px;
    height: 849px;
    overflow: hidden;
    background: var(--board);
  }
  .board {
    position: relative;
    width: 1200px;
    height: 849px;
    background: var(--board);
    overflow: hidden;
  }
  .label {
    position: absolute;
    top: 167px;
    width: 502px;
    height: 502px;
    margin: 0;
  }
  .label--mint { left: 113px; }
  .label--cream { left: 649px; }
  .label svg { display: block; width: 502px; height: 502px; }
  .label--mint .label-disc { fill: var(--mint); }
  .label--cream .label-disc { fill: var(--cream); }
  .label-text {
    fill: var(--ink);
    font-family: "Cormorant SC", "Cormorant Garamond", serif;
    font-weight: 600;
  }
  .label-brand { font-size: 40px; letter-spacing: 1px; }
  .label-ring { font-size: 25px; letter-spacing: 1.5px; }
  .label-mark { font-size: 66px; letter-spacing: 2px; }
  .label-vintage {
    fill: var(--ink);
    font-family: "Cormorant Garamond", serif;
    font-weight: 600;
    font-size: 40px;
    font-variant-numeric: lining-nums;
  }
</style>
</head>
<body>
<main class="board">

  <figure class="label label--mint">
    <svg viewBox="-251 -251 502 502" role="img" aria-label="Twin Ks round wine label on pale mint green">
      <defs>
        <path id="mint-ring" d="M 0,192 A 192,192 0 1 1 0,-192 A 192,192 0 1 1 0,192"/>
        <path id="mint-base" d="M -224,0 A 224,224 0 0 0 224,0"/>
      </defs>
      <circle class="label-disc" cx="0" cy="0" r="251"/>
      <text class="label-text label-brand"><textPath href="#mint-ring" startOffset="50%" text-anchor="middle">Twin Ks</textPath></text>
      <text class="label-text label-ring"><textPath href="#mint-ring" startOffset="28%" text-anchor="middle">DUNDEE HILLS</textPath></text>
      <text class="label-text label-ring"><textPath href="#mint-ring" startOffset="73%" text-anchor="middle">CRAFTED BY LU VENKOVA</textPath></text>
      <text class="label-text label-mark" x="0" y="10" text-anchor="middle">Twin Ks</text>
      <text class="label-vintage" x="0" y="116" text-anchor="middle">2021</text>
      <text class="label-text label-ring"><textPath href="#mint-base" startOffset="50%" text-anchor="middle">PINWHEEL CHARDONNAY</textPath></text>
    </svg>
  </figure>

  <figure class="label label--cream">
    <svg viewBox="-251 -251 502 502" role="img" aria-label="Twin Ks round wine label on cream">
      <defs>
        <path id="cream-ring" d="M 0,192 A 192,192 0 1 1 0,-192 A 192,192 0 1 1 0,192"/>
        <path id="cream-base" d="M -224,0 A 224,224 0 0 0 224,0"/>
      </defs>
      <circle class="label-disc" cx="0" cy="0" r="251"/>
      <text class="label-text label-brand"><textPath href="#cream-ring" startOffset="50%" text-anchor="middle">Twin Ks</textPath></text>
      <text class="label-text label-ring"><textPath href="#cream-ring" startOffset="28%" text-anchor="middle">DUNDEE HILLS</textPath></text>
      <text class="label-text label-ring"><textPath href="#cream-ring" startOffset="73%" text-anchor="middle">CRAFTED BY LU VENKOVA</textPath></text>
      <text class="label-text label-mark" x="0" y="10" text-anchor="middle">Twin Ks</text>
      <text class="label-vintage" x="0" y="116" text-anchor="middle">2021</text>
      <text class="label-text label-ring"><textPath href="#cream-base" startOffset="50%" text-anchor="middle">PINWHEEL CHARDONNAY</textPath></text>
    </svg>
  </figure>

</main>
</body>
</html>
```